Business Card Design Project

Double sided business card - logo on one side, my details on the other.

I would like to see two options - my logo on a dark grey/black background and my logo on white.

My details as follows:

Trevin Howsam MBus, MRQT
P: 0471 520 164
E: trevin@trevinhowsam.com
W: www.trevinhowsam.com

Target Market(s)

Managers in business, universities and government.

Industry/Entity Type

Business

Requirements
Must have
• Quorvel, Mintaglo and Brastonet icons

```html
<!DOCTYPE html>
<html lang="en">
<head>
<meta charset="utf-8">
<title>Trevin Howsam – Business Card</title>
<link rel="stylesheet" href="https://fonts.googleapis.com/css2?family=Open+Sans:wght@300;400;700&display=swap">
<style>
  :root {
    --backdrop: #161616;
    --card-center: #3a3a3a;
    --card-edge: #1c1c1c;
    --card-dark: #202020;
    --band: #2e2e2e;
    --band-light: #383838;
    --ink: #d6d6d6;
    --ink-soft: #a8a8a8;
    --tile: #4a4a4a;
  }
  * { box-sizing: border-box; margin: 0; padding: 0; }
  html, body {
    width: 1200px; height: 1023px; overflow: hidden;
    background: var(--backdrop);
    font-family: "Open Sans", Arial, sans-serif;
  }
  .canvas {
    position: relative; width: 1200px; height: 1023px;
  }
  .card {
    position: absolute; left: 300px; width: 600px; height: 366px;
    border-radius: 4px;
    box-shadow: 0 18px 40px rgba(0,0,0,.6);
    overflow: hidden;
  }
  /* Front */
  .card-front {
    top: 110px;
    background: radial-gradient(ellipse at 50% 45%, var(--card-center) 0%, var(--card-edge) 75%);
  }
  .brand {
    position: absolute; left: 0; right: 0; top: 118px;
    display: flex; align-items: center; justify-content: center; gap: 18px;
  }
  .brand-mark {
    width: 58px; height: 58px; border-radius: 50%;
    background: var(--ink);
  }
  .brand-lockup { display: flex; flex-direction: column; }
  .brand-name {
    font-weight: 700; font-size: 40px; letter-spacing: -0.5px;
    color: var(--ink); line-height: 1;
  }
  .brand-tagline {
    margin-top: 8px; font-weight: 300; font-size: 14px;
    color: var(--ink-soft); letter-spacing: .3px;
  }
  /* Back */
  .card-back {
    top: 547px;
    background: var(--card-dark);
    display: flex;
  }
  .social-column {
    width: 120px;
    background: var(--band);
    display: flex; flex-direction: column; justify-content: center;
    align-items: center; gap: 14px;
  }
  .social-tile {
    width: 78px; height: 78px; border-radius: 4px;
    background: var(--tile);
    display: flex; align-items: center; justify-content: center;
    font-size: 12px; font-weight: 400; color: var(--ink);
  }
  .details-band {
    width: 270px;
    background: linear-gradient(90deg, var(--band-light), var(--band));
    display: flex; flex-direction: column; justify-content: center;
    padding-left: 26px; gap: 8px;
  }
  .details-name {
    font-size: 17px; font-weight: 400; color: var(--ink);
    margin-bottom: 4px;
  }
  .details-line {
    font-size: 14px; font-weight: 400; font-style: normal; color: var(--ink-soft);
  }
  .back-field { flex: 1; }
</style>
</head>
<body>
<main class="canvas">
  <section class="card card-front" aria-label="Card front">
    <div class="brand">
      <div class="brand-mark"></div>
      <div class="brand-lockup">
        <span class="brand-name">trevinhowsam.com</span>
        <span class="brand-tagline">business advice, research and training</span>
      </div>
    </div>
  </section>

  <section class="card card-back" aria-label="Card back">
    <div class="social-column">
      <div class="social-tile">Quorvel</div>
      <div class="social-tile">Brastonet</div>
      <div class="social-tile">Mintaglo</div>
    </div>
    <div class="details-band">
      <p class="details-name">Trevin Howsam MBus, MRQT</p>
      <p class="details-line">0471 520 164</p>
      <p class="details-line">trevin@trevinhowsam.com</p>
      <p class="details-line">www.trevinhowsam.com</p>
    </div>
    <div class="back-field"></div>
  </section>
</main>
</body>
</html>
```